I need the design of a label for wine bottles, the design I leave at the free choice of the designer, it must contain the name of the winery that is: "Bodegas LT"

Bodegas LT

```html
<!DOCTYPE html>
<html lang="en">
<head>
<meta charset="utf-8">
<title>Bodegas LT – Wine Label</title>
<link rel="stylesheet" href="https://fonts.googleapis.com/css2?family=Bodoni+Moda:wght@400&family=Great+Vibes&display=swap">
<style>
  :root {
    --page-bg: #efece6;
    --label-mint: #e4efe6;
    --wine-pink: #b8395c;
    --wine-deep: #a32a4f;
    --wine-soft: #d97a93;
    --label-text: #fbeef1;
  }
  html, body {
    margin: 0;
    width: 1200px;
    height: 834px;
    overflow: hidden;
    background: var(--page-bg);
  }
  .canvas {
    position: relative;
    width: 1200px;
    height: 834px;
  }
  .wine-label {
    position: absolute;
    left: 365px;
    top: 104px;
    width: 470px;
    height: 626px;
    background: var(--label-mint);
    overflow: hidden;
    box-shadow: 0 2px 10px rgba(0,0,0,0.12);
  }
  .label-artwork {
    position: absolute;
    inset: 0;
    width: 100%;
    height: 100%;
  }
  .winery-name {
    position: absolute;
    left: 0;
    right: 0;
    top: 270px;
    margin: 0;
    text-align: center;
    font-family: "Bodoni Moda", serif;
    font-weight: 400;
    font-size: 46px;
    line-height: 60px;
    letter-spacing: 1px;
    color: var(--label-text);
  }
  .vintage {
    position: absolute;
    left: 0;
    right: 0;
    top: 408px;
    margin: 0;
    text-align: center;
    font-family: "Great Vibes", cursive;
    font-size: 32px;
    line-height: 44px;
    color: var(--label-text);
  }
  .quality-note {
    position: absolute;
    left: 0;
    right: 0;
    bottom: 10px;
    margin: 0;
    text-align: center;
    font-family: "Great Vibes", cursive;
    font-size: 18px;
    line-height: 24px;
    color: var(--label-text);
    opacity: 0.85;
  }
</style>
</head>
<body>
  <main class="canvas">
    <section class="wine-label">
      <svg class="label-artwork" viewBox="0 0 470 626" preserveAspectRatio="none" role="img" aria-label="Watercolour wash in wine pink with a faint grape leaf silhouette">
        <defs>
          <linearGradient id="base" x1="0" y1="0" x2="0" y2="1">
            <stop offset="0%" stop-color="var(--wine-pink)" stop-opacity="0"/>
            <stop offset="30%" stop-color="var(--wine-soft)" stop-opacity="0.35"/>
            <stop offset="60%" stop-color="var(--wine-pink)" stop-opacity="0.95"/>
            <stop offset="100%" stop-color="var(--wine-pink)"/>
          </linearGradient>
          <radialGradient id="wash" cx="50%" cy="50%" r="50%">
            <stop offset="0%" stop-color="var(--wine-deep)"/>
            <stop offset="55%" stop-color="var(--wine-pink)"/>
            <stop offset="80%" stop-color="var(--wine-soft)" stop-opacity="0.75"/>
            <stop offset="100%" stop-color="var(--wine-soft)" stop-opacity="0"/>
          </radialGradient>
        </defs>
        <rect x="0" y="0" width="470" height="626" fill="url(#base)"/>
        <ellipse cx="235" cy="250" rx="270" ry="250" fill="url(#wash)"/>
      </svg>
      <h1 class="winery-name">BODEGAS LT</h1>
      <p class="vintage">2019</p>
      <p class="quality-note">Premium Quality</p>
    </section>
  </main>
</body>
</html>
```